Essential Oil Blend Label Design

I need a label designed for our stress relief essential blend, Marlo's Drift.
The text for the front of the logo will be as follows:
"Marlo's Drift
All Natural Stress and Anxiety Relief
www.corvantglow.com"
Please make the front text small enough that it will show up in a picture of the bottle with the label is applied without being cut off on the edges. For reference, the label will be 4" x 2" and will go on these bottles:
http://www.brindlevessel.com/glass-bottles/european-dropper/amber/30ml-kqt30
On one of the sides of the label I would like this text, going up the label so that you turn the bottle sideways to read it (like in the attached label):
"Contains a pure, undiluted essential oil blend"
On the other side "For use in aromatherapy"
I would like this label to incorporate elements of a lush, green garden, like the Garden of Eden. The goal is for it convey peace and relaxation.
Please also note that I have attached the label for our other product for reference. The new label should be similar in its basic design as far as where the text is present and the overall style. My one problem with the attached label, though, is that the front text is a little too large and doesn't show up all the way in a picture. (I've attached the picture of the bottle as well so you can see what I mean).
I look forward to working with you!
Neil

```html
<!DOCTYPE html>
<html lang="en">
<head>
<meta charset="utf-8">
<title>Marlo's Drift – Label</title>
<link href="https://fonts.googleapis.com/css2?family=Cormorant+SC:wght@500;600&family=Ubuntu+Condensed&display=swap" rel="stylesheet">
<style>
  :root {
    --page: #ececec;
    --teal: #1f5b5d;
    --teal-deep: #144346;
    --teal-light: #2b6d6d;
    --leaf: #2f7a6c;
    --leaf-dark: #17504a;
    --gold: #d8c08a;
    --gold-soft: #c9b07a;
  }
  * { margin: 0; padding: 0; box-sizing: border-box; }
  html, body {
    width: 1200px;
    height: 1200px;
    overflow: hidden;
    background: var(--page);
  }
  .canvas {
    position: relative;
    width: 1200px;
    height: 1200px;
    display: flex;
    align-items: center;
    justify-content: center;
  }
  .label {
    position: relative;
    width: 1000px;
    height: 500px;
    overflow: hidden;
    background: var(--teal);
  }
  .label__garden {
    position: absolute;
    inset: 0;
    background:
      radial-gradient(ellipse 160px 260px at 12% 100%, rgba(47,122,108,0.55), transparent 70%),
      radial-gradient(ellipse 140px 300px at 30% 95%, rgba(23,80,74,0.6), transparent 70%),
      radial-gradient(ellipse 150px 280px at 70% 100%, rgba(47,122,108,0.5), transparent 70%),
      radial-gradient(ellipse 170px 250px at 88% 95%, rgba(23,80,74,0.6), transparent 70%),
      radial-gradient(ellipse 220px 160px at 35% 15%, rgba(43,109,109,0.45), transparent 70%),
      radial-gradient(ellipse 220px 160px at 68% 20%, rgba(43,109,109,0.45), transparent 70%),
      linear-gradient(90deg, var(--teal-deep) 0%, var(--teal) 30%, var(--teal-light) 50%, var(--teal) 70%, var(--teal-deep) 100%);
  }
  .label__side {
    position: absolute;
    top: 0;
    height: 100%;
    display: flex;
    align-items: center;
    justify-content: center;
    writing-mode: vertical-rl;
    transform: rotate(180deg);
    font-family: "Cormorant SC", serif;
    font-weight: 600;
    font-size: 18px;
    letter-spacing: 2px;
    color: var(--gold);
  }
  .label__side--left { left: 40px; }
  .label__side--right { right: 40px; }
  .label__front {
    position: absolute;
    left: 50%;
    top: 0;
    width: 440px;
    height: 100%;
    transform: translateX(-50%);
    display: flex;
    flex-direction: column;
    align-items: center;
    text-align: center;
    color: var(--gold);
  }
  .label__tree {
    margin-top: 56px;
    width: 200px;
    height: 100px;
    border-radius: 50% 50% 30% 30% / 60% 60% 40% 40%;
    background: radial-gradient(ellipse at 50% 40%, var(--gold) 0%, var(--gold-soft) 55%, rgba(201,176,122,0) 100%);
  }
  .label__name {
    margin-top: 70px;
    font-family: "Ubuntu Condensed", sans-serif;
    font-weight: 400;
    font-size: 46px;
    line-height: 1;
    color: var(--gold);
  }
  .label__tagline {
    margin-top: 44px;
    font-family: "Cormorant SC", serif;
    font-weight: 600;
    font-size: 26px;
    line-height: 1.3;
    letter-spacing: 2px;
  }
  .label__url {
    margin-top: 44px;
    font-family: "Ubuntu Condensed", sans-serif;
    font-weight: 400;
    font-size: 20px;
    letter-spacing: 0.5px;
  }
</style>
</head>
<body>
  <main class="canvas">
    <section class="label">
      <div class="label__garden" role="img" aria-label="Lush teal-green garden backdrop of tall grasses, leafy stems and soft foliage"></div>
      <p class="label__side label__side--left">Contains a pure, undiluted essential oil blend</p>
      <p class="label__side label__side--right">For use in aromatherapy</p>
      <div class="label__front">
        <div class="label__tree" role="img" aria-label="Gold illustration of a broad spreading garden tree"></div>
        <h1 class="label__name">Marlo's Drift</h1>
        <p class="label__tagline">All Natural Stress<br>and Anxiety Relief</p>
        <p class="label__url">www.corvantglow.com</p>
      </div>
    </section>
  </main>
</body>
</html>
```